Communication of Recommended Belief Letter

To Whom This May Concern,

My company's name is Bramwell LLC. I would like to send electronic messages to my clients. Therefore, I would like PixelHarbor to create a letterhead template to say Bramwell- without the LLC. My messages could extend up to 20 pages long. I would like something that is chic, fancy, and has creative designs. The background color should be white. The creative designs are open for suggestions without color restrictions. Font type and color are also open for suggestions. It may be what you believe best suite's the letterhead. I would like the letterhead to include the company logo. Please see attachment for file. Thank you.

Target Market(s)

working class American's

Industry/Entity Type

Communication

Contact Information for Business Card

The business card should be chic and fancy.

Font styles to use
Script

Requirements
Must have
• Company name: Bramwell LLC
• Company symbol: Please see attachment
• Name: Marisol Denby
• Title: President
• Company website: www.bramwellllc-example.com
Nice to have
• Open for suggestions

```html
<!DOCTYPE html>
<html lang="en">
<head>
<meta charset="utf-8">
<title>Bramwell Business Card</title>
<link rel="stylesheet" href="https://fonts.googleapis.com/css2?family=Cinzel:wght@400&family=Open+Sans:wght@400;600;700&display=swap">
<style>
  :root {
    --backdrop: #2b2d31;
    --gold-deep: #a8700a;
    --gold-mid: #d39a12;
    --gold-bright: #f2d23a;
    --gold-text: #a67a1c;
    --gold-line: #d4b21e;
    --card-white: #ffffff;
    --card-shade: #f1f1f1;
    --ink: #1d1d1d;
  }
  * { box-sizing: border-box; margin: 0; padding: 0; }
  html, body {
    width: 1200px; height: 864px; overflow: hidden;
    background: var(--backdrop);
  }
  .canvas {
    position: relative; width: 1200px; height: 864px;
  }
  .card {
    position: absolute; left: 320px; width: 560px; height: 320px;
    box-shadow: 0 10px 28px rgba(0,0,0,.45);
  }
  /* Front side */
  .card-front {
    top: 70px;
    background: radial-gradient(ellipse at 55% 38%, var(--gold-bright) 0%, var(--gold-mid) 42%, var(--gold-deep) 100%);
    display: flex; align-items: center; justify-content: center;
  }
  .front-emblem-area {
    position: absolute; left: 150px; top: 20px; width: 260px; height: 230px;
    border-radius: 50%;
    background: radial-gradient(circle, rgba(255,240,120,.55) 0%, rgba(255,220,60,.15) 60%, rgba(255,220,60,0) 100%);
  }
  .front-name {
    position: relative;
    font-family: "Cinzel", serif; font-weight: 400;
    font-size: 46px; letter-spacing: 1px;
    color: var(--card-white);
    margin-top: 90px;
  }
  /* Back side */
  .card-back {
    top: 470px;
    background: linear-gradient(160deg, var(--card-white) 0%, var(--card-white) 55%, var(--card-shade) 100%);
  }
  .brand {
    position: absolute; left: 190px; top: 34px;
    display: flex; align-items: center; gap: 14px;
  }
  .brand-dot {
    width: 34px; height: 34px; border-radius: 50%;
    background: var(--gold-mid);
  }
  .brand-name {
    font-family: "Cinzel", serif; font-weight: 400;
    font-size: 40px; color: var(--gold-text); line-height: 1;
  }
  .person {
    position: absolute; left: 36px; top: 104px;
    font-family: "Open Sans", sans-serif;
  }
  .person-name {
    font-weight: 700; font-size: 17px; color: var(--gold-text);
  }
  .person-title {
    font-size: 12.5px; color: var(--ink); margin-top: 1px;
  }
  .divider {
    position: absolute; left: 0; right: 0; top: 150px;
    height: 1px; background: var(--gold-line);
  }
  .contacts {
    position: absolute; right: 26px; top: 196px;
    list-style: none;
    font-family: "Open Sans", sans-serif; font-size: 14px; color: var(--ink);
    text-align: right;
  }
  .contacts li {
    display: flex; align-items: center; justify-content: flex-end;
    gap: 10px; height: 23px;
  }
  .contacts svg { width: 12px; height: 12px; fill: var(--gold-mid); flex: none; }
  .contacts .no-icon { padding-right: 22px; }
</style>
</head>
<body>
<main class="canvas">
  <section class="card card-front">
    <div class="front-emblem-area" role="img" aria-label="Soft gold glow where the company emblem decoration sits"></div>
    <h1 class="front-name">Bramwell</h1>
  </section>

  <section class="card card-back">
    <div class="brand">
      <span class="brand-dot"></span>
      <span class="brand-name">Bramwell</span>
    </div>
    <div class="person">
      <p class="person-name">Marisol Denby</p>
      <p class="person-title">President</p>
    </div>
    <div class="divider"></div>
    <ul class="contacts">
      <li>555 014 2790
        <svg viewBox="0 0 12 12"><path d="M2.5 1l2 2.3-1 1.2c.6 1.4 1.6 2.4 3 3l1.2-1 2.3 2-1 1.8C5 10.2 1.8 7 1 2z"/></svg>
      </li>
      <li>info@bramwellllc-example.com
        <svg viewBox="0 0 12 12"><path d="M0 2.5h12v7H0z M0.6 3l5.4 3.6L11.4 3" stroke="#fff" stroke-width=".8"/></svg>
      </li>
      <li>www.bramwellllc-example.com
        <svg viewBox="0 0 12 12"><circle cx="6" cy="6" r="5.5"/><path d="M.5 6h11M6 .5c-3 3-3 8 0 11M6 .5c3 3 3 8 0 11" stroke="#fff" stroke-width=".7" fill="none"/></svg>
      </li>
      <li class="no-icon">P.O. Box 1207, Elm Harbor, Maryland 20000</li>
    </ul>
  </section>
</main>
</body>
</html>
```